Decorative Candle business needs website designed

We are a new decorative candle business, and we need a website designed. We are looking for a modern/elegant feel to the page. We are working on taking pictures of each of our designs, so that we can display all our designs online.

Our target audience is females aged 16-45

We will need online store facilities also, as we plan to see online.

Please feel free to check out our instagram page for an idea of what we do: @waxworksbymirelle

I have attached our logo below for use.

```html
<!DOCTYPE html>
<html lang="en">
<head>
<meta charset="utf-8">
<title>Candles – Decorative Candle Store</title>
<link href="https://fonts.googleapis.com/css2?family=Source+Sans+3:wght@400;600;700&display=swap" rel="stylesheet">
<style>
  :root {
    --black: #0b0b0b;
    --pink: #e9588a;
    --pink-light: #f27aa3;
    --pink-dark: #c93f6e;
    --maroon: #6b1624;
    --maroon-deep: #4a0d18;
    --wine: #8a2136;
    --caption-bg: rgba(50, 10, 16, 0.82);
    --button: #c8476b;
    --white: #ffffff;
    --panel-border: #e2e2e2;
    --frame: #d9d9d9;
    --text-light: #f3dfe3;
  }
  * { box-sizing: border-box; margin: 0; padding: 0; }
  html, body { width: 814px; height: 1200px; overflow: hidden; background: var(--white); }
  body { position: relative; font-family: "Source Sans 3", Arial, sans-serif; color: var(--white); }
  .abs { position: absolute; }

  /* Header */
  .site-header { left: 0; top: 0; width: 814px; height: 78px; background: var(--black); }
  .brand { left: 26px; top: 18px; display: flex; align-items: center; gap: 8px; font-size: 22px; font-weight: 400; letter-spacing: 1px; color: var(--white); }
  .brand-dot { width: 12px; height: 12px; border-radius: 50%; background: var(--pink); }
  .search { left: 378px; top: 31px; width: 118px; height: 22px; background: var(--white); color: #111; font-size: 12px; font-weight: 600; padding: 3px 6px; }
  .search svg { position: absolute; right: 6px; top: 4px; }
  .social { display: flex; gap: 7px; }
  .social span { width: 20px; height: 20px; border-radius: 50%; background: var(--pink); display: block; }
  .header-social { left: 553px; top: 32px; }
  .cart { left: 716px; top: 28px; display: flex; gap: 10px; font-size: 10px; font-weight: 700; line-height: 1.25; }

  /* Navigation */
  .main-nav { left: 0; top: 78px; width: 814px; height: 44px; background: linear-gradient(var(--pink-light), var(--pink) 55%, var(--pink-dark)); }
  .nav-item { top: 0; height: 44px; line-height: 44px; font-size: 16px; font-weight: 700; text-align: center; transform: translateX(-50%); }
  .nav-sep { top: 0; width: 1px; height: 44px; background: rgba(255,255,255,0.45); }

  /* Hero */
  .hero { left: 0; top: 122px; width: 814px; height: 426px;
    background: radial-gradient(ellipse 190px 240px at 170px 260px, #ffd27a 0%, #f3a43a 35%, rgba(150,40,40,0) 75%), linear-gradient(120deg, #6a1820, #7e2230 50%, #5c141c); }
  .hero-caption { left: 369px; top: 266px; width: 382px; height: 150px; background: var(--caption-bg); padding: 24px 28px; }
  .hero-caption h2 { font-size: 35px; font-weight: 700; line-height: 1.05; margin-bottom: 8px; }
  .hero-caption p { font-size: 18px; line-height: 1.25; }
  .order-btn { left: 610px; top: 427px; width: 122px; height: 36px; background: var(--button); font-size: 17px; line-height: 36px; text-align: center; }
  .slider-dots { left: 354px; top: 526px; display: flex; gap: 9px; }
  .slider-dots span { width: 16px; height: 16px; border-radius: 50%; background: var(--white); }
  .slider-dots span.active { background: var(--wine); }

  /* Welcome band */
  .welcome { left: 0; top: 548px; width: 814px; height: 128px; text-align: center;
    background: linear-gradient(var(--maroon-deep), var(--wine) 45%, var(--maroon) 100%); padding-top: 24px; }
  .welcome h1 { font-size: 31px; font-weight: 400; color: var(--text-light); }
  .welcome p { font-size: 13px; line-height: 1.35; color: var(--text-light); }

  /* Panels */
  .panel { background: var(--white); border: 3px solid var(--panel-border); }
  .panel-title { background: var(--pink); color: var(--white); font-weight: 700; }
  .products-panel { left: 20px; top: 707px; width: 537px; height: 328px; }
  .products-title { left: 3px; top: 4px; width: 525px; height: 40px; font-size: 18px; line-height: 40px; padding-left: 14px; }
  .product-row { left: 11px; width: 508px; height: 115px; border: 2px solid var(--frame); }
  .product { top: 2px; width: 85px; }
  .product-photo { width: 85px; height: 85px; display: block; }
  .product-name { left: 0; width: 100%; height: 24px; background: var(--pink); }
  .product-label { top: 90px; font-size: 11px; font-weight: 700; color: var(--white); }

  .insta-panel { left: 587px; top: 706px; width: 185px; height: 292px; }
  .insta-title { left: 0; top: 0; width: 179px; height: 42px; padding: 4px 12px; line-height: 1; }
  .insta-title strong { display: block; font-size: 17px; }
  .insta-title small { font-size: 11px; }
  .insta-photo { width: 78px; height: 76px; }

  /* Footer */
  .site-footer { left: 0; top: 1064px; width: 814px; height: 136px; background: var(--maroon); }
  .footer-nav { left: 25px; top: 18px; font-size: 17px; color: var(--text-light); word-spacing: 3px; }
  .footer-nav b { font-weight: 400; margin: 0 8px; }
  .footer-text { left: 25px; top: 84px; font-size: 11px; font-weight: 600; color: var(--text-light); }
  .copyright { left: 0; top: 110px; width: 814px; text-align: center; font-size: 11px; color: var(--text-light); }
  .footer-social { left: 598px; top: 25px; }
  .newsletter-label { left: 598px; top: 57px; font-size: 10px; }
  .newsletter { left: 596px; top: 79px; display: flex; }
  .newsletter-input { width: 108px; height: 22px; background: var(--white); color: #333; font-size: 10px; font-weight: 600; padding: 4px 5px; }
  .newsletter-submit { width: 50px; height: 22px; background: var(--pink); font-size: 11px; font-weight: 700; text-align: center; line-height: 22px; }
</style>
</head>
<body>

<header class="site-header abs">
  <div class="brand abs"><span class="brand-dot"></span>Candles</div>
  <div class="search abs">Search
    <svg width="14" height="14" viewBox="0 0 14 14"><circle cx="5.5" cy="5.5" r="4" fill="none" stroke="#111" stroke-width="2"/><line x1="8.5" y1="8.5" x2="13" y2="13" stroke="#111" stroke-width="2.2"/></svg>
  </div>
  <div class="social header-social abs" aria-label="Social links"><span></span><span></span><span></span><span></span></div>
  <div class="cart abs">
    <svg width="24" height="20" viewBox="0 0 24 20"><path d="M1 2h4l3 11h12l3-8H7" fill="none" stroke="#fff" stroke-width="2.2"/><circle cx="9" cy="17" r="2" fill="#fff"/><circle cx="19" cy="17" r="2" fill="#fff"/></svg>
    <div>My Cart<br>0 Items</div>
  </div>
</header>

<nav class="main-nav abs">
  <span class="nav-sep abs" style="left:94px"></span>
  <span class="nav-item abs" style="left:138px">Home</span>
  <span class="nav-sep abs" style="left:196px"></span>
  <span class="nav-item abs" style="left:257px">Products</span>
  <span class="nav-sep abs" style="left:330px"></span>
  <span class="nav-item abs" style="left:391px">Store</span>
  <span class="nav-sep abs" style="left:452px"></span>
  <span class="nav-item abs" style="left:518px">Contact</span>
  <span class="nav-sep abs" style="left:581px"></span>
  <span class="nav-item abs" style="left:643px">About</span>
  <span class="nav-sep abs" style="left:701px"></span>
</nav>

<section class="hero abs" role="img" aria-label="Three lit pillar candles glowing against a dark red damask wall"></section>
<div class="hero-caption abs">
  <h2>New Candles</h2>
  <p>Neque porro quisquam est qui dolorem ipsum quia dolor sit amet</p>
</div>
<div class="order-btn abs">Order Now</div>
<div class="slider-dots abs"><span></span><span class="active"></span><span></span><span></span></div>

<section class="welcome abs">
  <h1>Welcome to Candles</h1>
  <p>Neque porro quisquam est qui dolorem ipsum quia dolor sit amet<br>Lorem ipsum dolor sit amet, consectetur adipiscing elit.</p>
</section>

<section class="products-panel panel abs">
  <h3 class="products-title panel-title abs">New Products</h3>

  <div class="product-row abs" style="top:52px">
    <div class="product-name abs" style="top:86px"></div>
    <div class="product abs" style="left:6px"><div class="product-photo" role="img" aria-label="Decorated candle product photo" style="background:linear-gradient(#6d5a4a,#c9b9a8)"></div><span class="product-label abs">Item Name</span></div>
    <div class="product abs" style="left:108px"><div class="product-photo" role="img" aria-label="Decorated candle product photo" style="background:linear-gradient(#5e4a3e,#d8ccbf)"></div><span class="product-label abs">Item Name</span></div>
    <div class="product abs" style="left:210px"><div class="product-photo" role="img" aria-label="Decorated candle product photo" style="background:linear-gradient(#4e3a30,#e2d8cc)"></div><span class="product-label abs">Item Name</span></div>
    <div class="product abs" style="left:311px"><div class="product-photo" role="img" aria-label="Decorated candle product photo" style="background:linear-gradient(#7a6a5c,#e6ded5)"></div><span class="product-label abs">Item Name</span></div>
    <div class="product abs" style="left:413px"><div class="product-photo" role="img" aria-label="Decorated candle product photo" style="background:linear-gradient(#5a4640,#b49c8e)"></div><span class="product-label abs">Item Name</span></div>
  </div>

  <div class="product-row abs" style="top:184px">
    <div class="product-name abs" style="top:86px"></div>
    <div class="product abs" style="left:6px"><div class="product-photo" role="img" aria-label="Decorated candle product photo" style="background:linear-gradient(#8a745e,#e3d8ca)"></div><span class="product-label abs">Item Name</span></div>
    <div class="product abs" style="left:108px"><div class="product-photo" role="img" aria-label="Decorated candle product photo" style="background:linear-gradient(#8c8080,#ddd6d4)"></div><span class="product-label abs">Item Name</span></div>
    <div class="product abs" style="left:210px"><div class="product-photo" role="img" aria-label="Decorated candle product photo" style="background:linear-gradient(#a08c70,#efe8de)"></div><span class="product-label abs">Item Name</span></div>
    <div class="product abs" style="left:311px"><div class="product-photo" role="img" aria-label="Decorated candle product photo" style="background:linear-gradient(#7a6660,#e8e0da)"></div><span class="product-label abs">Item Name</span></div>
    <div class="product abs" style="left:413px"><div class="product-photo" role="img" aria-label="Decorated candle product photo" style="background:linear-gradient(#6a7080,#c8b8a8)"></div><span class="product-label abs">Item Name</span></div>
  </div>
</section>

<aside class="insta-panel panel abs">
  <div class="insta-title panel-title abs"><strong>INSTAGRAM</strong><small>Latest Photos</small></div>
  <div class="insta-photo abs" style="left:6px;top:48px;background:#a87866" role="img" aria-label="Latest photo: dessert on a plate"></div>
  <div class="insta-photo abs" style="left:88px;top:48px;background:#cfc6bc" role="img" aria-label="Latest photo: tea set"></div>
  <div class="insta-photo abs" style="left:6px;top:128px;background:#d8c9a4" role="img" aria-label="Latest photo: baked treat"></div>
  <div class="insta-photo abs" style="left:88px;top:128px;background:#e27ba0" role="img" aria-label="Latest photo: pink heart candle"></div>
  <div class="insta-photo abs" style="left:6px;top:208px;background:#e0a8c0" role="img" aria-label="Latest photo: pink gift items"></div>
  <div class="insta-photo abs" style="left:88px;top:208px;background:#c4bcb4" role="img" aria-label="Latest photo: staircase decor"></div>
</aside>

<footer class="site-footer abs">
  <div class="footer-nav abs">Home<b>|</b>Products<b>|</b>Store<b>|</b>Contact<b>|</b>About</div>
  <p class="footer-text abs">Lorem ipsum dolor sit amet, consectetur adipiscing elit. Nulla malesuada</p>
  <p class="copyright abs">Copyright 2014 WaxworksByMirelle</p>
  <div class="social footer-social abs" aria-label="Social links"><span></span><span></span><span></span><span></span></div>
  <p class="newsletter-label abs">Sucribe To Our Newsletter</p>
  <div class="newsletter abs"><div class="newsletter-input">Enter your email</div><div class="newsletter-submit">Submit</div></div>
</footer>

</body>
</html>
```